"Harrow Crest Builders" is a residential building company and needs a new business card design and may re

We would like a redesign based on the existing logo, and would like to see a new font as well. We are bespoke home builders who build sustainable energy efficient homes.

Industry/Entity Type

Construction

Contact Information for Business Card

Business card size 40mm x 90mm

Colors

Designer to choose colors to be used in the design.

```html
<!DOCTYPE html>
<html lang="en">
<head>
<meta charset="utf-8">
<title>Harrow Crest Builders – Business Cards</title>
<link rel="stylesheet" href="https://fonts.googleapis.com/css2?family=Montserrat:wght@400;500;600&family=Work+Sans:wght@400;500&display=swap">
<style>
  :root {
    --backdrop: #2a2a2c;
    --card: #1e1e1f;
    --blue: #2c4a9e;
    --orange: #f5821f;
    --text: #d9d9d9;
    --muted: #9a9a9a;
  }
  * { box-sizing: border-box; margin: 0; padding: 0; }
  html, body { width: 1200px; height: 900px; overflow: hidden; }
  body {
    background: var(--backdrop);
    font-family: "Work Sans", sans-serif;
    position: relative;
  }
  .card {
    position: absolute;
    left: 240px;
    width: 720px;
    height: 320px;
    background: var(--card);
    box-shadow: 0 18px 40px rgba(0,0,0,0.45);
    overflow: hidden;
  }
  .card-front { top: 60px; display: flex; align-items: center; justify-content: center; }
  .card-back { top: 500px; }

  .wordmark {
    display: flex;
    align-items: center;
    gap: 14px;
  }
  .wordmark-square {
    width: 22px; height: 22px;
    background: var(--orange);
  }
  .wordmark-name {
    font-family: "Montserrat", sans-serif;
    font-weight: 600;
    font-size: 30px;
    letter-spacing: 2px;
    text-transform: uppercase;
    color: var(--blue);
  }
  .card-back .wordmark { position: absolute; left: 44px; top: 44px; }
  .card-back .wordmark-name { font-size: 26px; }

  .holder {
    position: absolute;
    right: 44px; top: 140px;
    text-align: right;
  }
  .holder-name {
    font-family: "Montserrat", sans-serif;
    font-weight: 600;
    font-size: 20px;
    letter-spacing: 0.5px;
    color: var(--blue);
    text-transform: uppercase;
  }
  .holder-role { font-size: 15px; color: var(--muted); margin-top: 4px; }
  .edge-tab {
    position: absolute;
    right: 0; top: 140px;
    width: 12px; height: 50px;
    background: var(--orange);
    border-radius: 8px 0 0 8px;
  }
  .divider {
    position: absolute;
    left: 44px; right: 44px; top: 204px;
    height: 2px; background: var(--orange);
  }
  .contacts {
    position: absolute;
    left: 44px; top: 218px;
    list-style: none;
    font-size: 15px;
    color: var(--text);
  }
  .contacts li { display: flex; align-items: center; gap: 12px; height: 24px; }
  .contacts svg { width: 14px; height: 14px; flex: none; }
  .address {
    position: absolute;
    right: 44px; top: 218px;
    text-align: right;
    font-size: 15px;
    line-height: 24px;
    color: var(--text);
  }
  .address .label { color: var(--blue); }
  .base-stripe {
    position: absolute; left: 0; right: 0; bottom: 0; height: 10px;
    display: flex;
  }
  .base-stripe .blue { width: 55%; background: var(--blue); }
  .base-stripe .orange { flex: 1; background: var(--orange); }
</style>
</head>
<body>
  <section class="card card-front">
    <div class="wordmark">
      <span class="wordmark-square"></span>
      <span class="wordmark-name">Harrow Crest Builders</span>
    </div>
  </section>

  <section class="card card-back">
    <div class="wordmark">
      <span class="wordmark-square"></span>
      <span class="wordmark-name">Harrow Crest Builders</span>
    </div>

    <div class="holder">
      <p class="holder-name">Daniel Mortlake</p>
      <p class="holder-role">Founder</p>
    </div>
    <span class="edge-tab"></span>

    <div class="divider"></div>

    <ul class="contacts">
      <li>
        <svg viewBox="0 0 16 16" aria-hidden="true"><path d="M4 1 L6.5 4 L5 6 Q7 10 10 11 L12 9.5 L15 12 L13 15 Q6 15 1 4 Z" fill="var(--orange)"/></svg>
        0400 555 013
      </li>
      <li>
        <svg viewBox="0 0 16 16" aria-hidden="true"><rect x="1" y="3" width="14" height="10" fill="var(--orange)"/><path d="M1 3 L8 9 L15 3" stroke="var(--card)" stroke-width="1.4" fill="none"/></svg>
        daniel@harrowcrestbuilders.com.au
      </li>
      <li>
        <svg viewBox="0 0 16 16" aria-hidden="true"><g fill="none" stroke="var(--orange)" stroke-width="1.4"><circle cx="8" cy="8" r="6.5"/><ellipse cx="8" cy="8" rx="3" ry="6.5"/><path d="M1.5 8 H14.5"/></g></svg>
        www.harrowcrestbuilders.com.au
      </li>
    </ul>

    <div class="address">
      <p>PO Box 4182 Northgate</p>
      <p>LPO Ashbury WA 6090</p>
      <p><span class="label">Reg:</span> -40873 | <span class="label">ABN:</span> 52 000 318 664</p>
    </div>

    <div class="base-stripe"><span class="blue"></span><span class="orange"></span></div>
  </section>
</body>
</html>
```